Dallan Whitford Band needs a top quality creative design for Album CD cover and digital music channe

I need an eye-catching CD cover and digital design for CD duplication for my new album. The music genre is Alternative rock which features lots of guitars and fast paced post-punk rock/pop music. I want something that is e2xciting and has a bit of attitude and dynamism perhaps with a bit of humour thrown in! Our band logo is orange and blue so it needs to blend with that. (logo attached). I haven't decided what the album will be titled as yet but tracks on the album include...."Keep Your Lantern Burning Low", "Driftwood", "Rain on Tuesday", "Hold the Line", "Under Paper Skies", " Past the Harbor", "Light the Engine",. You can hear some of the tracks on Soundcloud if that helps https://tunebarrel.example/dallanwhitford50

Target Market(s)

I want it to appeal to both male and female audiences primarily in the 25 - 55 year age group.

Industry/Entity Type

Digital

Colors
f37022
0355a3
3276b5
f68e4e

Requirements
Must have
• Eye catching, stand out on the shelf. Interesting. Makes a Statement.
Nice to have
• Incorporate the logo if possible.
Should not have
• Nothing political.

```html
<!DOCTYPE html>
<html lang="en">
<head>
<meta charset="utf-8">
<title>Dallan Whitford Band — Fragment of Wanderlust</title>
<link rel="stylesheet" href="https://fonts.googleapis.com/css2?family=Raleway:wght@200;700&display=swap">
<style>
  :root {
    --paper: #ffffff;
    --orange: #f37022;
    --orange-soft: #f68e4e;
    --navy: #1f3a66;
    --blue: #0355a3;
    --ink-light: #ffffff;
  }
  html, body {
    margin: 0;
    padding: 0;
    width: 1200px;
    height: 1200px;
    overflow: hidden;
    background: var(--paper);
  }
  .cover {
    position: relative;
    width: 1200px;
    height: 1200px;
    background: var(--paper);
    font-family: "Raleway", sans-serif;
  }
  .shard-field {
    position: absolute;
    left: 80px;
    top: 93px;
    width: 1067px;
    height: 1054px;
    background:
      radial-gradient(ellipse 45% 40% at 40% 35%, rgba(31,58,102,0.85), rgba(31,58,102,0) 70%),
      radial-gradient(ellipse 35% 45% at 72% 62%, rgba(31,58,102,0.8), rgba(31,58,102,0) 70%),
      linear-gradient(135deg, var(--orange) 0%, var(--orange-soft) 45%, var(--orange) 100%);
  }
  .band-badge {
    position: absolute;
    left: 380px;
    top: 380px;
    width: 440px;
    height: 440px;
    border-radius: 50%;
    background: var(--navy);
    box-shadow: 0 6px 18px rgba(0,0,0,0.35);
    display: flex;
    align-items: center;
    justify-content: center;
  }
  .band-name {
    margin: 0;
    color: var(--ink-light);
    font-weight: 700;
    font-size: 50px;
    line-height: 1.2;
    text-align: center;
    text-transform: uppercase;
    letter-spacing: 1px;
  }
  .title-rule {
    position: absolute;
    left: 50px;
    top: 992px;
    width: 1097px;
    height: 2px;
    background: rgba(255,255,255,0.75);
  }
  .album-title {
    position: absolute;
    left: 84px;
    top: 958px;
    margin: 0;
    width: 1080px;
    color: var(--ink-light);
    font-weight: 200;
    font-size: 52px;
    line-height: 70px;
    letter-spacing: 16px;
    white-space: nowrap;
    text-transform: uppercase;
  }
</style>
</head>
<body>
  <main class="cover">
    <div class="shard-field" role="img" aria-label="Shattered field of orange and navy blue geometric shards"></div>
    <div class="band-badge">
      <h1 class="band-name">Dallan<br>Whitford<br>Band</h1>
    </div>
    <div class="title-rule"></div>
    <h2 class="album-title">Fragment of Wanderlust</h2>
  </main>
</body>
</html>
```